Logo and business card

RVK Financial Solutions - Branding & Image Project

There will be 3 companies in our group. We want a similar Branding look & feel for all 3. The first company is DLW Financial which is already established, and I have included samples of the branding.

The goal for this design project is to create the corporate branding for RVK Financial Solutions which is the second company in the group.

Please use the same colours and fonts that we use at DLW Financial but the logo must be different. The final design should communicate financial safety and growth. Our typical clients are 40+ years and financially conservative.

Can you create a sample version using the dark green in the attached image.

We will need print resolution files and low res file for email, web etc.

The main printed outputs we need are – see separate attachment for examples;
Business Card 2 sided
Web logo

We’ll then need the following
Letterhead & follow on sheets
Envelopes C5 2 sided & C4 2 sided
Compliment Slips

```html
<!DOCTYPE html>
<html lang="en">
<head>
<meta charset="utf-8">
<title>RVK Financial Solutions – Business Card</title>
<link href="https://fonts.googleapis.com/css2?family=Tinos&display=swap" rel="stylesheet">
<style>
  :root {
    --backdrop: #e9e6e1;
    --card-white: #ffffff;
    --navy-teal: #1d4f6a;
    --bright-teal: #2aa3a8;
    --rule: #8fa3b1;
    --deep-teal: #1b4653;
    --glow-teal: #2eaab8;
    --name-light: #e3f1f2;
  }
  html, body {
    margin: 0;
    width: 900px;
    height: 1200px;
    overflow: hidden;
    background: var(--backdrop);
  }
  .canvas { position: relative; width: 900px; height: 1200px; }

  .serif { font-family: "Tinos", "Times New Roman", serif; }

  .card {
    position: absolute;
    left: 120px;
    width: 663px;
    height: 437px;
    box-shadow: 0 4px 12px rgba(0,0,0,0.25);
  }
  .card--front { top: 128px; background: var(--card-white); }
  .card--back {
    top: 636px;
    background: linear-gradient(215deg, var(--glow-teal) 0%, #25808e 35%, var(--deep-teal) 70%, var(--deep-teal) 100%);
  }

  .company-name {
    position: absolute;
    margin: 0;
    font-weight: 400;
    line-height: 1;
    white-space: nowrap;
  }
  .card--front .company-name {
    right: 37px; top: 78px;
    font-size: 32px;
    color: var(--navy-teal);
  }
  .card--back .company-name {
    left: 0; right: 0; top: 200px;
    text-align: center;
    font-size: 34px;
    color: var(--name-light);
  }

  .holder-name {
    position: absolute; left: 42px; top: 188px;
    font-size: 25px; color: var(--navy-teal);
  }
  .holder-title {
    position: absolute; left: 42px; top: 221px;
    font-size: 13px; color: var(--bright-teal);
  }
  .holder-rule {
    position: absolute; left: 190px; top: 232px;
    width: 436px; height: 1px; background: var(--rule);
  }

  .contact-list {
    position: absolute; left: 42px; top: 249px;
    margin: 0; padding: 0; list-style: none;
    font-size: 14px; color: var(--navy-teal);
  }
  .contact-list li { display: flex; align-items: center; height: 19px; }
  .contact-list svg { width: 11px; height: 11px; margin-right: 8px; fill: var(--bright-teal); }

  .office-address {
    position: absolute; right: 37px; top: 249px;
    margin: 0; font-style: normal; text-align: right;
    font-size: 14px; line-height: 19px; color: var(--navy-teal);
  }

  .regulatory-note {
    position: absolute; left: 0; right: 0; top: 343px;
    margin: 0; text-align: center;
    font-size: 14px; line-height: 18px; color: var(--navy-teal);
  }
</style>
</head>
<body>
<main class="canvas">

  <section class="card card--front" aria-label="Business card front">
    <p class="company-name serif">RVK Financial Solutions</p>

    <div class="holder-name serif">Morgan Ellery</div>
    <div class="holder-title serif">Senior Wealth Adviser</div>
    <div class="holder-rule"></div>

    <ul class="contact-list serif">
      <li>
        <svg viewBox="0 0 12 12" aria-hidden="true"><path d="M2.4 0.5 L4.3 2.6 L3.4 4.2 C4.1 5.7 6.3 7.9 7.8 8.6 L9.4 7.7 L11.5 9.6 L10.3 11.3 C6 11.6 0.4 6 0.7 1.7 Z"/></svg>
        01632 960418
      </li>
      <li>
        <svg viewBox="0 0 12 12" aria-hidden="true"><path d="M3 0 H9 A1 1 0 0 1 10 1 V11 A1 1 0 0 1 9 12 H3 A1 1 0 0 1 2 11 V1 A1 1 0 0 1 3 0 Z M3.4 1.5 V9.5 H8.6 V1.5 Z"/></svg>
        07700 900274
      </li>
      <li>
        <svg viewBox="0 0 12 12" aria-hidden="true"><path d="M0.5 2.5 H11.5 V3.2 L6 6.8 L0.5 3.2 Z M0.5 4.4 L6 8 L11.5 4.4 V9.8 H0.5 Z"/></svg>
        Morgan.ellery@rvkfs.co.uk
      </li>
      <li>
        <svg viewBox="0 0 12 12" aria-hidden="true"><path d="M6 0.5 A5.5 5.5 0 1 0 6 11.5 A5.5 5.5 0 1 0 6 0.5 Z M6 1.6 C6.8 2.4 7.3 3.8 7.4 5.4 H4.6 C4.7 3.8 5.2 2.4 6 1.6 Z M1.7 5.4 A4.4 4.4 0 0 1 4.4 1.9 C3.9 2.9 3.6 4.1 3.5 5.4 Z M8.5 5.4 C8.4 4.1 8.1 2.9 7.6 1.9 A4.4 4.4 0 0 1 10.3 5.4 Z M1.7 6.6 H3.5 C3.6 7.9 3.9 9.1 4.4 10.1 A4.4 4.4 0 0 1 1.7 6.6 Z M4.6 6.6 H7.4 C7.3 8.2 6.8 9.6 6 10.4 C5.2 9.6 4.7 8.2 4.6 6.6 Z M8.5 6.6 H10.3 A4.4 4.4 0 0 1 7.6 10.1 C8.1 9.1 8.4 7.9 8.5 6.6 Z"/></svg>
        www.rvkfs.co.uk
      </li>
    </ul>

    <address class="office-address serif">
      The Mill House, Unit 4<br>
      Larkfield Business Park<br>
      Brookside Road, Ashwell<br>
      Baldock, Herts, SG7 5QT
    </address>

    <p class="regulatory-note serif">
      RVK Financial Solutions Limited is authorised and regulated by the Financial Conduct Authority<br>
      Reference 581034<br>
      Registered in England and Wales No. 639207
    </p>
  </section>

  <section class="card card--back" aria-label="Business card back">
    <p class="company-name serif">RVK Financial Solutions</p>
  </section>

</main>
</body>
</html>
```